LITTLE DESIGN WORK REQUIRED!

UPDATE: WE WEREN'T OVERLY ECSTATIC WITH THE DESIGNS WE WERE RECEIVING SO WE DID MOST OF THE DESIGN WORK OURSELVES...

PLEASE SEE THE NEWLY ATTACHED PPT DOC TO VIEW NEARLY EXACT REPLICAS OF WHAT WE WANT THE SITE TO LOOK LIKE. WE NOW NEED YOUR HELP TO MAKE IT LOOK LIKE SOMETHING WORTHY OF THE WEB.

NO CODING REQUIRED - EXPECTED OUTPUT PSD FILES

Hi everyone!

We're looking for a designer to work their magic for our site! We're a not-for-profit program aimed at helping young people realise their potential!

In the attached PPT file, you'll notice we've already DESIGNED THE ENTIRE SITE IN POWERPOINT. Now, we need YOU to make the small changes we requested in the document as well as design the whole thing in psd.

Any questions, don't hesitate to ask.

Brook-Rise
Updates

We've done about 95% of the design for you. Please fine-tune it. See the newly attached PPT doc for details. 

The best two designs will win. This project closes on Friday - please message us if you are absolutely sure you cannot make the deadline.

Thanks,
Brook-Rise

```html
<!DOCTYPE html>
<html lang="en">
<head>
<meta charset="utf-8">
<title>Brook-Rise</title>
<link href="https://fonts.googleapis.com/css2?family=Russo+One&family=Arimo:ital,wght@0,400;0,700;1,400&display=swap" rel="stylesheet">
<style>
:root{
  --page:#dfe6da;
  --bar:#4a4a4a;
  --green:#7fbb12;
  --green-dark:#5f9a05;
  --green-deep:#3f6e00;
  --ink:#333;
  --muted:#777;
  --line:#d6ddd2;
  --card:#fff;
  --tag:#1f2e06;
  --link:#2a4f8f;
  --soft:#f7f8f6;
}
*{box-sizing:border-box;margin:0;padding:0}
html,body{width:1200px;height:1071px;overflow:hidden}
body{background:var(--page);font-family:"Arimo",Arial,sans-serif;color:var(--ink);position:relative}
.abs{position:absolute}
.top-bar{left:0;top:0;width:1200px;height:26px;background:var(--bar)}
.holes{display:flex;justify-content:space-around;align-items:center;background:#e9e9e9}
.holes span{width:10px;height:10px;border-radius:50%;background:#555}
.logo-card{left:155px;top:0;width:218px;height:107px;background:var(--card);box-shadow:0 2px 3px rgba(0,0,0,.15)}
.logo-card .holes{height:14px;background:transparent}
.logo-card .holes span{width:8px;height:8px;background:#777}
.brand{position:absolute;left:20px;top:44px;display:flex;align-items:center;gap:8px;font-family:"Russo One",sans-serif;font-size:27px;color:#1d1d1d}
.brand i{width:16px;height:16px;background:var(--green);display:block}
.main-nav{left:393px;top:42px;display:flex;align-items:center;height:26px;font-size:13px;text-transform:uppercase}
.home-btn{width:30px;height:26px;background:var(--green);border-radius:3px;display:flex;align-items:center;justify-content:center;margin-right:17px}
.main-nav a{color:#222;text-decoration:none;margin-right:36px}
.search{left:889px;top:42px;width:156px;height:26px;background:#fff;border:1px solid #e2e2e2;border-radius:2px;font-size:12px;color:#999;padding:6px 8px}
.search svg{position:absolute;right:6px;top:5px}
.hero{left:155px;top:135px;width:672px;height:217px;border-radius:8px 0 0 8px;background:linear-gradient(160deg,#6aa804 0%,#80c010 45%,#5d9a02 100%);overflow:hidden}
.hero-title{left:29px;top:38px;font-family:"Russo One",sans-serif;font-size:23px;color:#111;letter-spacing:1px}
.hero-lines{left:25px;top:82px;width:500px;font-family:"Russo One",sans-serif;font-size:15px;line-height:20px;color:var(--green);letter-spacing:.5px}
.hero-lines span{background:#111;padding:1px 4px;box-decoration-break:clone;-webkit-box-decoration-break:clone}
.hero-lines b{color:#111;font-weight:400;letter-spacing:-1px}
.promo{left:827px;top:135px;width:218px;height:217px;background:#fff;border-radius:0 8px 8px 0;text-align:center;font-family:"Russo One",sans-serif;color:#444;overflow:hidden}
.promo .holes{height:27px;background:#e6e6e6}
.promo-title{margin-top:20px;font-size:24px;letter-spacing:1.5px}
.signup{display:inline-block;margin-top:9px;background:var(--green);color:#fff;font-size:15px;padding:4px 8px;border-radius:4px;letter-spacing:1px}
.promo-line{font-size:15px;letter-spacing:1.5px;margin-top:18px}
.slider-nav{left:175px;top:352px;display:flex;font-size:11px;background:#fff;border:1px solid #ccc;border-top:none;border-radius:0 0 6px 6px;height:21px}
.slider-nav span{padding:4px 9px;color:#555}
.slider-nav span+span{border-left:1px solid #ddd}
.slider-nav em{color:var(--green);font-style:normal}
.content-card{left:155px;top:396px;width:890px;height:640px;background:var(--card);border-radius:8px;border:1px solid #cfd6cb;overflow:hidden}
.intro{left:14px;top:17px;width:610px;font-size:13px;line-height:17px;color:#333}
.intro p+p{margin-top:14px}
.intro strong{color:var(--green);font-weight:400}
.pillar{top:122px;height:75px;text-align:center}
.pillar .box{position:absolute;left:0;right:0;bottom:0;height:51px;background:#ececec;border:1px solid #ddd;font-family:"Russo One",sans-serif;font-size:21px;color:#444;line-height:49px;letter-spacing:.5px}
.pillar .box::before,.pillar .box::after{content:"";position:absolute;top:4px;width:3px;height:3px;background:#aaa;border-radius:50%}
.pillar .box::before{left:4px}.pillar .box::after{right:4px}
.pillar .badge{position:absolute;left:50%;top:0;transform:translateX(-50%);width:40px;height:40px;border-radius:50%;background:#ececec;display:flex;align-items:flex-start;justify-content:center;padding-top:6px;z-index:1}
.posts-head{left:0;top:246px;width:646px;height:42px;background:#4d4d4d;color:#fff;font-family:"Russo One",sans-serif;font-size:20px;padding:10px 16px;letter-spacing:.5px}
.post-image{left:0;top:288px;width:440px;height:228px;background:radial-gradient(ellipse at 40% 40%,#84c20e,#6aa803)}
.post-tag{left:0;top:288px;width:121px;height:46px;background:var(--tag);color:#fff;font-size:12px;padding:8px 14px;line-height:15px}
.post-tag i{display:block}
.post-side{left:440px;top:288px;width:206px;height:228px;background:#f5f6f4}
.post-excerpt{left:16px;top:12px;width:182px;font-size:13px;font-weight:700;line-height:16px;color:#444}
.shares{left:16px;top:106px;display:flex;gap:8px;font-size:10px;align-items:center}
.pill{border:1px solid #bbb;background:#fff;padding:2px 5px;border-radius:2px;color:#2a4f8f;display:flex;align-items:center;gap:3px}
.pill i{width:9px;height:9px;background:#4a90c2;display:block}
.pill.like i{background:#3b5998}
.count{border:1px solid #ccc;background:#fff;padding:2px 7px;color:#333}
.topics{left:16px;top:179px;font-size:10px;color:#444;line-height:13px}
.topics a{color:#333}
.read-more{left:125px;top:199px;background:var(--green);color:#fff;font-size:11px;padding:3px 6px;border-radius:2px;font-weight:700}
.load-more{left:0;top:531px;width:646px;height:18px}
.load-more .rule{position:absolute;left:0;right:0;top:4px;height:8px;border-top:1px solid #ccc;border-bottom:1px solid #ccc}
.load-more span{position:absolute;left:293px;top:0;background:#c7cbc4;color:#fff;font-size:11px;padding:3px 7px;border-radius:2px}
.sidebar{left:646px;top:0;width:244px;height:560px;border-left:1px solid var(--line)}
.side-head{position:absolute;left:0;width:244px;border-bottom:1px solid var(--line);font-size:13px;color:#333;padding-left:12px;display:flex;align-items:center;gap:6px}
.side-row{position:absolute;left:0;width:244px;border-bottom:1px solid var(--line);font-size:10px;line-height:12px}
.login{left:10px;top:14px;display:flex;gap:8px;color:#888;font-size:9px;line-height:11px}
.login b{background:#3b5998;color:#fff;font-size:11px;padding:4px 6px;border:1px solid #29487d;height:22px}
.feed{padding:7px 10px;display:flex;gap:8px}
.feed .thumb{width:30px;height:30px;background:#5a77b0;flex:none}
.feed .thumb.pale{background:#c5cde0}
.feed a{color:var(--link);font-weight:700;font-size:10px;display:block}
.feed small{color:#666;font-size:10px}
.popular{padding:13px 12px 0 10px;color:#999;display:flex;gap:8px}
.popular em{color:var(--green);font-style:normal}
.amb{padding:5px 10px;display:flex;gap:8px}
.amb .thumb{width:40px;height:40px;background:linear-gradient(#e3e8ef,#c9d2dd);flex:none;border:1px solid #ddd}
.amb b{color:var(--green);font-size:13px;font-weight:400;display:block}
.amb i{color:#444;font-size:11px;display:block}
.footer{left:0;top:560px;width:890px;height:80px;border-top:1px solid var(--line)}
.footer-nav{left:16px;top:22px;display:flex;gap:15px;font-size:11px;text-transform:uppercase;color:#333}
.footer-nav .on{color:var(--green)}
.copy{left:16px;top:51px;font-size:11px}
.copy u{text-decoration:underline}
.follow{left:702px;top:20px;font-size:11px}
.follow-icons{display:flex;gap:4px;margin-top:8px}
.follow-icons i{width:14px;height:14px;display:block;border-radius:2px}
</style>
</head>
<body>
<div class="abs top-bar"></div>

<header>
  <div class="abs logo-card">
    <div class="holes"><span></span><span></span><span></span><span></span><span></span><span></span><span></span><span></span></div>
    <div class="brand"><i></i>BROOK RISE</div>
  </div>
  <nav class="abs main-nav">
    <span class="home-btn"><svg width="14" height="13" viewBox="0 0 14 13"><path d="M7 0 0 6h2v7h4V9h2v4h4V6h2z" fill="#fff"/></svg></span>
    <a href="#">About us</a><a href="#">Resources</a><a href="#">Workshops</a><a href="#">Ambassadors</a>
  </nav>
  <div class="abs search">Enter Keyword
    <svg width="14" height="14" viewBox="0 0 14 14"><circle cx="6" cy="6" r="4.5" fill="none" stroke="#ccc" stroke-width="1.6"/><path d="M9 9l4 4" stroke="#ccc" stroke-width="2"/></svg>
  </div>
</header>

<section class="abs hero" role="img" aria-label="Snowy mountain range under a starry sky, tinted green">
  <h1 class="abs hero-title">BROOK-RISE</h1>
  <p class="abs hero-lines"><span>IS A NOT-FOR-PROFIT PROGRAM AIMED AT HELPING PEOPLE ESPECIALLY YOUNG PEOPLE REALISE THEIR POTENTIAL AND ACHIEVE SUCCESS.</span><b> ▸▸▸▸▸▸▸▸▸▸▸▸▸▸▸▸▸▸▸▸▸▸▸▸▸▸▸▸▸▸▸▸▸</b></p>
</section>
<aside class="abs promo">
  <div class="holes"><span></span><span></span><span></span><span></span><span></span><span></span><span></span><span></span><span></span></div>
  <div class="promo-title">KILIMANJARO</div>
  <div class="signup">SIGN-UP</div>
  <div class="promo-line">FOR OUR</div>
  <div class="promo-line">BROOK-RISE FEATS</div>
</aside>
<div class="abs slider-nav"><span><em>←</em> Prev</span><span>Next <em>→</em></span></div>

<main class="abs content-card">
  <div class="abs intro">
    <p><strong>Brook-rise</strong> is a not-for-profit program aimed at helping people – especially young people – realise their potential and achieve success.</p>
    <p><strong>Our resources</strong> are categorised into four areas: discovery, design, build, and achieve – what we believe are the four steps in the achievement framework we teach.</p>
  </div>

  <div class="abs pillar" style="left:26px;width:133px">
    <span class="badge"><svg width="30" height="18" viewBox="0 0 30 18"><ellipse cx="15" cy="9" rx="14" ry="8" fill="#444"/><circle cx="15" cy="9" r="5" fill="#ececec"/><circle cx="15" cy="9" r="2.5" fill="#444"/></svg></span>
    <div class="box">DISCOVER</div>
  </div>
  <div class="abs pillar" style="left:188px;width:117px">
    <span class="badge"><svg width="26" height="24" viewBox="0 0 26 24"><path d="M13 23 2 12A6 6 0 0 1 13 4a6 6 0 0 1 11 8z" fill="#444"/></svg></span>
    <div class="box">DESIGN</div>
  </div>
  <div class="abs pillar" style="left:333px;width:117px">
    <span class="badge"><svg width="26" height="26" viewBox="0 0 26 26"><path d="M16 2a7 7 0 0 0-6 9L2 19l4 4 8-8a7 7 0 0 0 9-6l-4 2-3-3 2-4z" fill="#444"/></svg></span>
    <div class="box">BUILD</div>
  </div>
  <div class="abs pillar" style="left:487px;width:133px">
    <span class="badge"><svg width="28" height="28" viewBox="0 0 28 28"><path d="M7 2h14v8a7 7 0 0 1-14 0z" fill="#444"/><path d="M7 4H2v3a5 5 0 0 0 5 5M21 4h5v3a5 5 0 0 1-5 5" fill="none" stroke="#444" stroke-width="2"/><rect x="12" y="16" width="4" height="6" fill="#444"/><rect x="8" y="22" width="12" height="4" fill="#444"/></svg></span>
    <div class="box">ACHIEVE</div>
  </div>

  <h2 class="abs posts-head">RECENT POSTS</h2>
  <div class="abs post-image" role="img" aria-label="Featured image for the first post"></div>
  <div class="abs post-tag">FIRST<i>by Tom Harwell</i></div>
  <div class="abs post-side">
    <p class="abs post-excerpt">Lorem ipsum dolor sit amet, consectetur adipisicing elit, sed do eiusmod tempor incididunt ut labore et dolore magna aliqua.</p>
    <div class="abs shares">
      <span class="pill"><i></i>Chirp</span><span class="count">7</span>
      <span class="pill like"><i></i>Like</span><span class="count" style="padding:2px 4px">3</span>
    </div>
    <div class="abs topics">TOPICS:<br><a href="#">Innovation,</a><br><a href="#">Creative Blocks</a></div>
    <div class="abs read-more">Read More →</div>
  </div>
  <div class="abs load-more"><div class="rule"></div><span>Load More Posts</span></div>

  <aside class="abs sidebar">
    <div class="side-head" style="top:0;height:35px">Chatterbox Feed</div>
    <div class="side-row" style="top:35px;height:50px">
      <div class="abs login"><b>Login</b><span>You need to be logged into chatterbox<br>to see recent activity</span></div>
    </div>
    <div class="side-row feed" style="top:85px;height:44px"><span class="thumb"></span><div><a href="#">Chatterbox Developers</a><small>91,452 people recommend this.</small></div></div>
    <div class="side-row feed" style="top:129px;height:42px"><span class="thumb pale"></span><div><a href="#">Introducing iframe Tabs for Pages</a><small>138 people recommend this.</small></div></div>
    <div class="side-row feed" style="top:171px;height:43px"><span class="thumb"></span><div><a href="#">Like Button</a><small>87,345 people recommend this.</small></div></div>
    <div class="side-head" style="top:214px;height:31px"><svg width="14" height="14" viewBox="0 0 14 14"><path d="M7 0l2 5h5l-4 3 2 6-5-4-5 4 2-6-4-3h5z" fill="#f2c21b"/></svg>What's popular ?</div>
    <div class="side-row popular" style="top:245px;height:45px;background:var(--soft)"><em>→</em><span>Lorem ipsum dosectetur adipisicing elit, sed do.</span></div>
    <div class="side-row popular" style="top:290px;height:44px;background:var(--soft)"><em>→</em><span>Lorem ipsum dosectetur adipisicing elit, sed do.</span></div>
    <div class="side-row popular" style="top:334px;height:45px;background:var(--soft)"><em>→</em><span>Lorem ipsum dosectetur adipisicing elit, sed do.</span></div>
    <div class="side-row popular" style="top:379px;height:45px;background:var(--soft)"><em>→</em><span>Lorem ipsum dosectetur adipisicing elit, sed do.</span></div>
    <div class="side-head" style="top:424px;height:32px"><svg width="14" height="14" viewBox="0 0 14 14"><circle cx="7" cy="4" r="3.5" fill="#555"/><path d="M1 14a6 5 0 0 1 12 0z" fill="#3b5998"/></svg>Ambassadors</div>
    <div class="side-row amb" style="top:456px;height:54px"><span class="thumb" role="img" aria-label="Ambassador portrait"></span><div><b>Kiran Malde</b><i>Young web &amp; UI designer</i><i>→ Meet Kiran</i></div></div>
    <div class="side-row amb" style="top:510px;height:50px;border-bottom:none"><span class="thumb" role="img" aria-label="Ambassador portrait"></span><div><b>Kiran Malde</b><i>Young web &amp; UI designer</i><i>→ Meet Kiran</i></div></div>
  </aside>

  <footer class="abs footer">
    <nav class="abs footer-nav"><span class="on">Home</span><span>About us</span><span>Resources</span><span>Workshops</span><span>Ambassadors</span><span>Contact</span></nav>
    <div class="abs copy">© <u>BROOKRISE</u></div>
    <div class="abs follow">FOLLOW US :
      <div class="follow-icons">
        <i style="background:#3b5998"></i><i style="background:#4ab3e0"></i><i style="background:#222"></i><i style="background:#5b7fb8"></i><i style="background:#333"></i><i style="background:#4a7bd0"></i><i style="background:#5a9b3a"></i><i style="background:#bbb"></i>
      </div>
    </div>
  </footer>
</main>
</body>
</html>
```